bottle label/ product label for smoothies (ultra fresh)

Please create a bottle label for our smoothies for retail distribution.
It's important that the following key features are clearly stated:

Ultra-fresh

Handmade

No preservatives

Not heat-treated

No added sugar

The base of the product label should be transparent, so that the color and content of the smoothie can be seen clearly.

We are a young, dynamic company. Our values are honesty, ultra-freshness, and authenticity — and we are the only ones producing this type of product in our country. We are positioned in the premium segment.

Design style: Modern, clean, and natural — but not playful or childish.

Example product: Kelu Kelu (Mango, Pineapple, Lemon, Passion Fruit, Orange)

Wenn du möchtest, kann ich auch gleich einen konkreten Vorschlag für das Etikettendesign auf Englisch oder einen Entwurfstext für das Label selbst erstellen. Sag einfach Bescheid!

Target Market(s)

trade - convenience

Industry/Entity Type

trade

Font styles to use
Sans Serif

Requirements
Must have
• sales- features: Ultra-fresh Handmade No preservatives Not heat-treated No added sugar

```html
<!DOCTYPE html>
<html lang="en">
<head>
<meta charset="utf-8">
<title>Solvera Smoothie Label – Dieline</title>
<link rel="stylesheet" href="https://fonts.googleapis.com/css2?family=Montserrat:wght@300;500;600;700&family=Rubik:wght@800&family=Roboto:wght@400;500&family=PT+Sans&display=swap">
<style>
:root{
  --red:#ff0000;
  --orange:#ff7722;
  --white:#ffffff;
  --label-base:#b9b9b9;
  --ink:#111111;
  --dim-gold:#ffbb00;
}
*{box-sizing:border-box;margin:0;padding:0}
html,body{width:1200px;height:1000px;overflow:hidden;background:var(--white)}
.sheet{position:relative;width:1200px;height:1000px;font-family:"PT Sans",sans-serif;color:var(--ink)}
.abs{position:absolute}
.dims{position:absolute;left:0;top:0}
.dim-label{position:absolute;font-size:15px;transform:translateX(-50%);white-space:nowrap}
.dim-tag{background:var(--dim-gold);padding:1px 5px}
.dim-vertical{transform:translate(-50%,-50%) rotate(-90deg)}
.note-transparent{position:absolute;left:50px;top:366px;transform:translate(-50%,-50%) rotate(-90deg);font-size:15px;line-height:18px;text-align:center;white-space:nowrap}

.label{position:absolute;left:102px;top:293px;width:991px;height:425px;background:var(--label-base);overflow:hidden;color:var(--white);font-family:"Montserrat",sans-serif}
.band{position:absolute;left:0;width:100%;height:10px;background:var(--orange)}
.band-top{top:0}.band-bottom{bottom:0}
.center-x{transform:translateX(-50%);text-align:center;white-space:nowrap}

.brand{font-weight:600;letter-spacing:1px}
.brand-left{left:128px;top:32px;font-size:44px;line-height:50px}
.ingredients{left:133px;top:108px;width:150px;font-size:12px;font-weight:700;line-height:18.2px;text-align:center;transform:translateX(-50%)}
.ingredients h3{font-size:13px;font-weight:700;margin-bottom:1px}
.volume-chip{background:var(--white);color:var(--orange);font-weight:700;font-size:16px;line-height:25px;padding:0 9px}
.volume-left{left:98px;top:316px;width:70px;text-align:center}
.maker{left:136px;top:346px;font-size:12px;font-weight:700;line-height:18.2px}
.brand-vertical{left:292px;top:213px;font-size:96px;line-height:96px;font-weight:700;transform:translate(-50%,-50%) rotate(-90deg);white-space:nowrap;letter-spacing:2px}

.brand-center{left:498px;top:47px;font-size:36px;line-height:40px}
.tagline{left:498px;top:90px;font-size:11px;font-weight:300;letter-spacing:6px}
.smoothie{font-weight:300;letter-spacing:1px}
.smoothie-center{left:498px;top:104px;font-size:40px}
.ultra{font-family:"Rubik",sans-serif;font-weight:800}
.ultra-center{left:498px;top:140px;font-size:41px}
.fruit-art{left:373px;top:190px;width:226px;height:126px;border-radius:60px;background:radial-gradient(circle at 70% 55%,var(--orange) 0 40%,var(--red) 70%)}
.handmade{left:398px;top:190px;width:62px;height:62px;border-radius:50%;background:var(--white);color:var(--red);font-family:"Rubik",sans-serif;font-weight:800;font-size:14px;line-height:14px;display:flex;align-items:center;justify-content:center;text-align:center}
.claim{position:absolute;background:var(--white);color:var(--orange);font-size:10px;font-weight:700;line-height:11px;padding:0 6px;box-shadow:2px 2px 0 var(--red);white-space:nowrap}
.volume-center{left:461px;top:366px;width:83px;height:25px;background:var(--orange);font-size:20px;font-weight:700;line-height:25px;text-align:center;clip-path:polygon(0 0,100% 0,90% 100%,0 100%)}

.smoothie-right{left:855px;top:28px;font-size:25px}
.ultra-right{left:855px;top:51px;font-size:24px}
.nutrition{left:768px;top:98px;width:181px;height:258px;border:1.5px solid var(--white);padding:3px 3px;font-family:"Roboto",sans-serif;font-size:7.5px;line-height:9.5px;overflow:hidden}
.nutrition h2{font-family:"Montserrat",sans-serif;font-size:16px;font-weight:700;line-height:18px}
.nutrition .sub{font-weight:500;font-size:8px;border-bottom:5px solid var(--white);padding-bottom:2px;margin-bottom:2px}
.row{display:flex;justify-content:space-between;border-bottom:1px solid var(--white);padding:0.5px 0;font-weight:500}
.row.indent{padding-left:15px;font-weight:400}
.row.thick{border-bottom-width:4px}
.row.right{justify-content:flex-end}
.foot{font-size:7px;margin-top:4px;white-space:nowrap}
.cert{position:absolute;top:368px;width:30px;height:30px;border:2px solid var(--white);border-radius:50%}
.cert-shield{border-radius:6px 6px 15px 15px;width:27px}
</style>
</head>
<body>
<main class="sheet">

  <svg class="dims" width="1200" height="1000" viewBox="0 0 1200 1000" fill="none" stroke="#111" stroke-width="1">
    <defs>
      <marker id="tip" markerWidth="6" markerHeight="6" refX="5" refY="3" orient="auto-start-reverse">
        <path d="M0,0 L6,3 L0,6 z" fill="#111" stroke="none"/>
      </marker>
    </defs>
    <line x1="101" y1="177" x2="101" y2="193"/><line x1="1093" y1="177" x2="1093" y2="193"/>
    <line x1="104" y1="185" x2="1090" y2="185" marker-start="url(#tip)" marker-end="url(#tip)"/>
    <line x1="101" y1="268" x2="101" y2="284"/><line x1="371" y1="268" x2="371" y2="284"/>
    <line x1="824" y1="268" x2="824" y2="284"/><line x1="1093" y1="268" x2="1093" y2="284"/>
    <line x1="104" y1="277" x2="368" y2="277" marker-start="url(#tip)" marker-end="url(#tip)"/>
    <line x1="375" y1="277" x2="821" y2="277" marker-start="url(#tip)" marker-end="url(#tip)"/>
    <line x1="827" y1="277" x2="1090" y2="277" marker-start="url(#tip)" marker-end="url(#tip)"/>
    <line x1="79" y1="293" x2="96" y2="293"/><line x1="79" y1="718" x2="96" y2="718"/>
    <line x1="101" y1="725" x2="101" y2="742"/><line x1="1093" y1="725" x2="1093" y2="742"/>
    <line x1="1099" y1="718" x2="1116" y2="718"/>
    <line x1="1130" y1="294" x2="1154" y2="294"/><line x1="1130" y1="718" x2="1154" y2="718"/>
    <line x1="1146" y1="297" x2="1146" y2="715" marker-start="url(#tip)" marker-end="url(#tip)"/>
    <line x1="1105" y1="294" x2="1130" y2="294"/><line x1="1105" y1="315" x2="1130" y2="315"/>
    <line x1="1117" y1="296" x2="1117" y2="313" marker-start="url(#tip)" marker-end="url(#tip)"/>
    <polyline points="110,416 110,358 72,358" marker-end="url(#tip)"/>
  </svg>

  <span class="dim-label dim-tag" style="left:597px;top:156px">175mm</span>
  <span class="dim-label" style="left:244px;top:256px">47.5mm</span>
  <span class="dim-label" style="left:594px;top:256px">80mm</span>
  <span class="dim-label" style="left:967px;top:256px">47.5mm</span>
  <span class="dim-label dim-tag dim-vertical" style="left:1170px;top:506px">75mm</span>
  <span class="dim-label dim-vertical" style="left:1129px;top:304px;font-size:11px">4mm</span>
  <p class="note-transparent">Transparent<br>Background</p>

  <section class="label" aria-label="Smoothie bottle label">
    <div class="band band-top"></div>

    <div class="abs brand brand-left center-x">Solvera</div>
    <div class="abs ingredients">
      <h3>Ingredients:</h3>
      Navel Oranges, Ice (water), Plain Lowfat Yogurt (cultured Pas-teurized Lowfat Milk, Whey Protein Concen-trate, Nonfat Milk Solids, And Whey), Orange Juice Concen-trate, Vanilla Extract.
    </div>
    <div class="abs volume-chip volume-left">300ml</div>
    <div class="abs maker center-x">Manufactured by:<br>Company Name<br>Address:</div>
    <div class="abs brand brand-vertical">Solvera</div>

    <div class="abs brand brand-center center-x">Solvera</div>
    <div class="abs tagline center-x">test every drop</div>
    <div class="abs smoothie smoothie-center center-x">SMOOTHIE</div>
    <div class="abs ultra ultra-center center-x">Ultra-fresh</div>
    <div class="abs fruit-art" role="img" aria-label="Illustration of oranges, an orange half and an orange with a leaf"></div>
    <div class="abs handmade">HAND<br>MADE</div>
    <span class="claim" style="left:391px;top:328px">No preservatives</span>
    <span class="claim" style="left:503px;top:328px">Not Heat-treated</span>
    <span class="claim" style="left:448px;top:339px">No added sugar</span>
    <div class="abs volume-center">300ml</div>

    <div class="abs smoothie smoothie-right center-x">SMOOTHIE</div>
    <div class="abs ultra ultra-right center-x">Ultra-fresh</div>
    <div class="abs nutrition">
      <h2>Nutrition Facts</h2>
      <div class="sub">Healthy Orange Juice Smoothie</div>
      <div class="row">Amount Per Serving</div>
      <div class="row thick"><span>Calories 171</span><span>Calories from Fat 18</span></div>
      <div class="row right">% Daily Value*</div>
      <div class="row"><span>Total Fat 2g</span><span>3%</span></div>
      <div class="row indent"><span>Saturated Fat 0g</span><span>0%</span></div>
      <div class="row"><span>Cholesterol 2mg</span><span>1%</span></div>
      <div class="row"><span>Sodium 74mg</span><span>3%</span></div>
      <div class="row"><span>Potassium 561mg</span><span>16%</span></div>
      <div class="row"><span>Total Carbohydrates 31g</span><span>10%</span></div>
      <div class="row indent"><span>Dietary Fiber 5g</span><span>20%</span></div>
      <div class="row indent"><span>Sugar 20g</span><span></span></div>
      <div class="row thick"><span>Protein 6g</span><span>12%</span></div>
      <div class="row"><span>Vitamin A</span><span>11.6%</span></div>
      <div class="row"><span>Vitamin C</span><span>94.3%</span></div>
      <div class="row"><span>Calcium</span><span>14%</span></div>
      <div class="row"><span>Iron</span><span>6.3%</span></div>
      <div class="foot">*Percent Daily Value are based on a 2000 calorie diet.</div>
    </div>
    <div class="cert cert-shield" style="left:804px"></div>
    <div class="cert" style="left:841px"></div>
    <div class="cert" style="left:884px"></div>

    <div class="band band-bottom"></div>
  </section>
  <svg class="abs" style="left:99px;top:303px" width="6" height="404"><line x1="3" y1="0" x2="3" y2="404" stroke="#111" stroke-width="1.5" stroke-dasharray="6 4"/></svg>

  <div class="abs" style="left:91px;top:775px;width:58px;height:35px;background:var(--red);border:1px solid #111;font-size:16px;line-height:33px;text-align:center">Red</div>
  <div class="abs" style="left:165px;top:775px;width:57px;height:35px;background:var(--orange);font-size:16px;line-height:35px;text-align:center">Orange</div>
  <div class="abs" style="left:241px;top:775px;width:57px;height:35px;border:1px solid #111;font-size:16px;line-height:33px;text-align:center">White</div>
  <span class="dim-label" style="left:120px;top:812px;font-size:16px">1</span>
  <span class="dim-label" style="left:193px;top:812px;font-size:16px">2</span>
  <span class="dim-label" style="left:270px;top:812px;font-size:16px">3</span>
  <div class="abs" style="left:318px;top:775px;width:235px;height:35px;border:2px dashed var(--dim-gold);font-size:16px;line-height:31px;padding-left:16px">Width:175mm X Hight:75mm</div>

</main>
</body>
</html>
```